Hotel Business Card Project

Amber Crest Hotel will be a premium boutique hotel in Dhaka, Bangladesh. The hotel will offer the finest amenities and facilities available on the market, and the cost per room investment will far exceed other 5-star hotels currently in the market.

As a result, we wanted the business card to reflect that premium/luxurious/upscale feel, and also be elegant and hospitable at the same time.

The name 'Amber Crest' is derived from the fact that Bangladesh has 6 distinct seasons (you can get more information online if required, or contact me about it). The leaves in the logo has the tree because trees give people shade, protection and safety (just like our hotel would try to give).

Target Market(s)

Business professionals, guests

Industry/Entity Type

Investment

Requirements
Must have
• Elegant, Classy and very attractive business card.

Must be editable to enter specific Names, Positions, Phone numbers and email later on.
Nice to have
• The address would be: House 42, Road 57, Banani 4, Dhaka 1230, Bangladesh

Slogan- Luxury Redefined

```html
<!DOCTYPE html>
<html lang="en">
<head>
<meta charset="utf-8">
<title>Amber Crest Hotel — Business Card</title>
<link rel="stylesheet" href="https://fonts.googleapis.com/css2?family=Alegreya:ital,wght@0,500;1,500;1,700&family=Crimson+Text&family=Didact+Gothic&display=swap">
<style>
  :root {
    --amber: #fdb733;
    --amber-deep: #f7aa22;
    --pale: #fff3a0;
    --cream: #ffe9a8;
    --white: #ffffff;
    --ink: #1d1d1d;
    --gold-text: #9a7a2c;
    --slogan: #9c5b2b;
    --stage-light: #9a9a98;
    --stage-dark: #5c5c5c;
  }
  * { box-sizing: border-box; margin: 0; padding: 0; }
  html, body { width: 837px; height: 1200px; overflow: hidden; }
  body {
    position: relative;
    background: linear-gradient(135deg, var(--stage-light) 0%, #8a8a88 45%, var(--stage-dark) 100%);
    font-family: "Alegreya", serif;
  }
  .card {
    position: absolute;
    left: 55px;
    width: 713px;
    height: 476px;
    overflow: hidden;
    box-shadow: 3px 4px 8px rgba(0,0,0,0.45);
  }

  /* Front */
  .card-front { top: 64px; background: var(--amber); }
  .front-decoration {
    position: absolute;
    left: 0; right: 0; bottom: 0;
    height: 165px;
    background:
      radial-gradient(ellipse 55% 70% at 72% 30%, rgba(255,243,160,0.55), transparent 70%),
      linear-gradient(180deg, rgba(255,243,160,0) 0%, rgba(255,243,160,0.65) 55%, var(--pale) 100%);
  }
  .brand {
    position: absolute;
    left: 0; right: 0; top: 150px;
    text-align: center;
    color: var(--white);
    font-family: "Alegreya", serif;
    font-weight: 500;
  }
  .brand-mark {
    width: 92px; height: 92px;
    margin: 0 auto 22px;
    border-radius: 50%;
    background: var(--white);
  }
  .brand-name {
    font-size: 50px;
    letter-spacing: 1px;
    line-height: 1;
    text-transform: uppercase;
  }
  .brand-sub {
    margin-top: 6px;
    font-size: 16px;
    letter-spacing: 3px;
    text-transform: uppercase;
  }
  .front-slogan {
    position: absolute;
    right: 16px; bottom: 10px;
    font-style: italic;
    font-weight: 700;
    font-size: 30px;
    color: var(--slogan);
  }

  /* Back */
  .card-back { top: 663px; background: var(--white); }
  .photo-slot {
    position: absolute;
    left: 15px; top: 25px;
    width: 173px; height: 176px;
    border: 1.5px solid var(--ink);
    border-radius: 2px;
    display: flex; align-items: center; justify-content: center;
    font-family: "Crimson Text", serif;
    font-size: 17px;
    color: var(--ink);
  }
  .contact-fields {
    position: absolute;
    left: 15px; top: 276px;
    font-style: italic;
    font-weight: 700;
    font-size: 25px;
    line-height: 27px;
    color: var(--gold-text);
    list-style: none;
  }
  .info-panel {
    position: absolute;
    left: 442px; top: 0;
    width: 254px; height: 100%;
    background: var(--amber);
    color: var(--cream);
    text-align: right;
    padding-right: 10px;
  }
  .panel-name {
    position: absolute;
    right: 10px; top: 220px;
    font-style: italic;
    font-weight: 700;
    font-size: 29px;
    white-space: nowrap;
  }
  .panel-slogan {
    position: absolute;
    right: 10px; top: 253px;
    font-style: italic;
    font-weight: 500;
    font-size: 18px;
  }
  .panel-address {
    position: absolute;
    right: 10px; top: 400px;
    font-family: "Didact Gothic", sans-serif;
    font-style: normal;
    font-size: 17px;
    line-height: 21px;
  }
</style>
</head>
<body>
  <section class="card card-front">
    <div class="front-decoration" role="img" aria-label="Soft pale-yellow swirls and floral flourish across the lower edge"></div>
    <div class="brand">
      <div class="brand-mark"></div>
      <div class="brand-name">Amber Crest</div>
      <div class="brand-sub">Hotel</div>
    </div>
    <p class="front-slogan">Luxury Redefined</p>
  </section>

  <section class="card card-back">
    <div class="photo-slot">Insert picture here</div>
    <ul class="contact-fields">
      <li>Name</li>
      <li>Position</li>
      <li>Phone number</li>
      <li>Email Address</li>
    </ul>
    <div class="info-panel">
      <p class="panel-name">Amber Crest Hotel</p>
      <p class="panel-slogan">Luxury Redefined</p>
      <address class="panel-address">House 42, Road 57,<br>Banani 4, Dhaka 1230,<br>Bangladesh</address>
    </div>
  </section>
</body>
</html>
```